Traffic product supplier - Temporary Raised Pavement Markers

We need a flyer design that will grab the customer's eye to the product (TRPMs) and entice curiosity to the business. Showing 1 product but promoting other products. The following information should be included:
- Logo (attached)
- Sale Product image (Temporary Road Pavement Marker AKA Press and Holds)
- Product wording (attached word document)

Happy for you to add/amend wording for grammatical purpose and other images that show it is a sale flyer.

Background on KLV - We are a thermoplastic manufacturer for road markings and traffic product supplier. KLV specializes in producing high quality hotmelt thermoplastic that meet Australian Standard AS4049.2. We are able to produce other specifications as required by the customer.

Would like the colour scheme to be similar to the logo.

If you need more information let me know.

Target Market(s)

Asphalt industry / road builders

Font styles to use
Serif
Sans Serif

Requirements
Must have
• - Kelvoro Lane Ventures (My company name)
- Contact details:
- 02 8417 2530
- marcus.t@klvsupplyco.com.au
- info@klvsupplyco.com.au
-www.klvmtq.com

- Attached images.
-Title (Temporary Road Pavement Markers)

```html
<!DOCTYPE html>
<html lang="en">
<head>
<meta charset="UTF-8">
<title>KLV – Temporary Road Pavement Markers</title>
<link rel="stylesheet" href="https://fonts.googleapis.com/css2?family=Oswald:wght@500;700&family=Montserrat:wght@600;700&family=Roboto:ital,wght@0,400;0,700;1,400&display=swap">
<style>
  :root{
    --blue:#1565c0;
    --blue-dark:#0d4fa0;
    --yellow:#fcc419;
    --dark:#1f2320;
    --panel:#e2e2e2;
    --ink:#2b2b2b;
    --white:#ffffff;
  }
  *{margin:0;padding:0;box-sizing:border-box;}
  html,body{width:900px;height:1200px;overflow:hidden;background:#fff;}
  .flyer{position:relative;width:900px;height:1200px;overflow:hidden;background:var(--white);font-family:"Roboto",Arial,sans-serif;color:var(--ink);}

  /* header */
  .brand{position:absolute;left:66px;top:30px;width:190px;text-align:center;}
  .brand-mark{display:flex;align-items:center;justify-content:center;gap:12px;}
  .brand-square{width:38px;height:38px;background:var(--blue);}
  .brand-name{font-family:"Oswald",sans-serif;font-weight:700;font-size:66px;line-height:1;color:var(--blue);}
  .brand-tagline{margin-top:14px;font-size:11px;font-style:italic;color:#333;white-space:nowrap;}

  .hero-band{position:absolute;left:0;top:173px;width:900px;height:370px;background:var(--dark);}
  .hero-photo{position:absolute;left:290px;top:0;width:610px;height:543px;
    clip-path:polygon(15% 0,100% 0,100% 100%,0 100%,0 32%);
    background:
      linear-gradient(90deg,rgba(31,35,32,1) 0%,rgba(31,35,32,.55) 22%,rgba(31,35,32,0) 45%),
      linear-gradient(180deg,#3c6ea8 0%,#8aa9c4 30%,#c9a77a 48%,#4a4a42 62%,#c2603a 80%,#2c302b 100%);}
  .hero-product{position:absolute;left:445px;top:360px;width:412px;height:155px;border-radius:4px;
    background:linear-gradient(90deg,#e9b72a 0%,#e9b72a 32%,#e7e4e0 34%,#f2f0ee 100%);}

  .title{position:absolute;left:40px;top:212px;font-family:"Oswald",sans-serif;font-weight:700;font-size:80px;line-height:71px;letter-spacing:1px;text-transform:uppercase;}
  .title span{display:block;}
  .title .light{color:var(--white);}
  .title .accent{color:var(--yellow);}

  /* product cards */
  .product-card{position:absolute;left:37px;width:290px;height:136px;border:1px solid #bbb;background:#fff;}
  .product-card .product-image{position:absolute;left:60px;top:18px;width:165px;height:78px;}
  .product-card .product-label{position:absolute;left:0;bottom:0;width:100%;height:20px;background:var(--yellow);font-size:12px;text-align:center;line-height:20px;color:#333;}
  .card-red{top:586px;} .card-red .product-image{background:linear-gradient(180deg,#c8323a 0 18%,#f1efee 18% 100%);}
  .card-white{top:746px;} .card-white .product-image{background:linear-gradient(180deg,#b9c0c8 0 20%,#eceef0 20% 100%);}
  .card-yellow{top:907px;} .card-yellow .product-image{background:linear-gradient(180deg,#f0b21e 0 25%,#e8ad1f 25% 100%);}

  /* info panel */
  .info-panel{position:absolute;left:352px;top:586px;width:508px;height:454px;background:var(--panel);}
  .section-tab{position:absolute;left:-2px;height:36px;background:var(--blue);color:var(--white);
    font-family:"Montserrat",sans-serif;font-weight:700;font-size:19px;line-height:36px;padding-left:28px;border-radius:0 18px 18px 0;
    border-top:3px solid var(--blue-dark);}
  .tab-about{top:14px;width:182px;}
  .tab-details{top:151px;width:275px;}
  .section-text{position:absolute;left:31px;width:455px;font-size:12.5px;line-height:16px;color:#333;}
  .about-text{top:64px;}
  .details-text{top:200px;}
  .feature-list{position:absolute;left:31px;top:284px;width:460px;list-style:none;}
  .feature-list li{position:relative;padding-left:22px;font-size:12px;font-weight:700;line-height:15px;margin-bottom:7px;color:#222;}
  .feature-list svg{position:absolute;left:0;top:1px;}

  .price-box{position:absolute;left:6px;top:392px;width:190px;height:60px;background:var(--blue);border:2px solid #fff;color:#fff;
    font-family:"Montserrat",sans-serif;font-weight:700;font-size:40px;line-height:56px;text-align:center;}
  .price-box sup{font-size:18px;vertical-align:18px;}
  .price-note{position:absolute;left:205px;top:392px;width:303px;height:60px;background:var(--yellow);
    font-family:"Oswald",sans-serif;font-weight:500;font-size:36px;line-height:60px;text-align:center;color:#1b1b1b;}

  /* footer */
  .footer{position:absolute;left:0;top:1098px;width:900px;height:102px;}
  .footer svg.footer-bands{position:absolute;left:0;top:0;}
  .contact-tab{position:absolute;left:62px;top:-10px;width:228px;height:38px;background:var(--blue);border-radius:10px 10px 0 0;border-top:3px solid var(--blue-dark);
    color:#fff;font-family:"Montserrat",sans-serif;font-weight:600;font-size:22px;line-height:35px;text-align:center;}
  .phone{position:absolute;left:40px;top:42px;display:flex;align-items:center;gap:14px;font-family:"Montserrat",sans-serif;font-weight:700;font-size:31px;color:#111;}
  .emails{position:absolute;left:377px;top:24px;font-family:"Montserrat",sans-serif;font-weight:600;font-size:13px;color:#fff;line-height:26px;}
  .emails div,.website{display:flex;align-items:center;gap:10px;}
  .divider{position:absolute;left:643px;top:40px;width:2px;height:30px;background:#fff;}
  .website{position:absolute;left:670px;top:42px;font-family:"Montserrat",sans-serif;font-weight:700;font-size:17px;color:#fff;}
</style>
</head>
<body>
<div class="flyer">

  <header class="brand">
    <div class="brand-mark"><span class="brand-square"></span><span class="brand-name">KLV</span></div>
    <p class="brand-tagline">"Marking Safer Lanes for Every Journey"</p>
  </header>

  <div class="hero-band"></div>
  <div class="hero-photo" role="img" aria-label="City skyline at dusk with light trails on a freeway"></div>
  <div class="hero-product" role="img" aria-label="Yellow, red and white temporary road pavement markers"></div>

  <h1 class="title">
    <span class="light">Temporary</span>
    <span class="accent">Road</span>
    <span class="light">Pavement</span>
    <span class="accent">Markers</span>
  </h1>

  <div class="product-card card-red">
    <div class="product-image" role="img" aria-label="Temporary pavement marker with red reflective strip"></div>
    <div class="product-label">Temp RPM - Red</div>
  </div>
  <div class="product-card card-white">
    <div class="product-image" role="img" aria-label="White temporary pavement marker"></div>
    <div class="product-label">Temp RPM - White</div>
  </div>
  <div class="product-card card-yellow">
    <div class="product-image" role="img" aria-label="Yellow temporary pavement marker"></div>
    <div class="product-label">Temp RPM - Yellow</div>
  </div>

  <section class="info-panel">
    <div class="section-tab tab-about">ABOUT US</div>
    <p class="section-text about-text">Temporary road pavement markers, also known as press 'n' holds, are a great short-term solution to mark asphalt and pavements before permanent line marking takes place. They provide a way to delineate lanes and edges before the permanent longitudinal line marking process takes place.</p>

    <div class="section-tab tab-details">PRODUCT DETAILS</div>
    <p class="section-text details-text">TRPMs or press 'n' holds are available in yellow or white and come with a Class 1A reflective strip applied to tough high impact plastic. They are an economical solution for making newly laid roads safer. An easy to remove clear cover protects the reflective film during sealing and is easily ripped off afterwards.</p>

    <ul class="feature-list">
      <li><svg width="13" height="13" viewBox="0 0 13 13"><rect x="0.5" y="0.5" width="12" height="12" fill="none" stroke="#1565c0"/><path d="M3 6.5l2.5 2.5L10 3.5" fill="none" stroke="#1565c0" stroke-width="1.6"/></svg>Dimensions: 100 mm long x 50 mm high x 25 mm wide</li>
      <li><svg width="13" height="13" viewBox="0 0 13 13"><rect x="0.5" y="0.5" width="12" height="12" fill="none" stroke="#1565c0"/><path d="M3 6.5l2.5 2.5L10 3.5" fill="none" stroke="#1565c0" stroke-width="1.6"/></svg>Double sided Class 1A Reflective</li>
      <li><svg width="13" height="13" viewBox="0 0 13 13"><rect x="0.5" y="0.5" width="12" height="12" fill="none" stroke="#1565c0"/><path d="M3 6.5l2.5 2.5L10 3.5" fill="none" stroke="#1565c0" stroke-width="1.6"/></svg>Clear cover for reflective protection</li>
      <li><svg width="13" height="13" viewBox="0 0 13 13"><rect x="0.5" y="0.5" width="12" height="12" fill="none" stroke="#1565c0"/><path d="M3 6.5l2.5 2.5L10 3.5" fill="none" stroke="#1565c0" stroke-width="1.6"/></svg>Available in all white, and red (reflective strip) and white, all yellow and all blue</li>
    </ul>

    <div class="price-box"><sup>$</sup>0.40</div>
    <div class="price-note">EX GST PER TRPM</div>
  </section>

  <footer class="footer">
    <svg class="footer-bands" width="900" height="102" viewBox="0 0 900 102">
      <polygon points="0,0 345,0 315,102 0,102" fill="#fcc419"/>
      <polygon points="345,0 900,0 900,102 315,102" fill="#1565c0"/>
    </svg>
    <div class="contact-tab">CONTACT US</div>
    <div class="phone">
      <svg width="24" height="24" viewBox="0 0 24 24"><path d="M6.6 10.8a15 15 0 006.6 6.6l2.2-2.2c.3-.3.7-.4 1-.2 1.1.4 2.3.6 3.6.6.6 0 1 .4 1 1V20c0 .6-.4 1-1 1A17 17 0 013 4c0-.6.4-1 1-1h3.5c.6 0 1 .4 1 1 0 1.3.2 2.5.6 3.6.1.3 0 .7-.2 1z" fill="#1565c0"/></svg>
      02 8417 2530
    </div>
    <div class="emails">
      <div><svg width="16" height="12" viewBox="0 0 16 12"><rect width="16" height="12" rx="1" fill="#fff"/><path d="M1 1l7 5 7-5" fill="none" stroke="#1565c0" stroke-width="1.4"/></svg>marcus.t@klvsupplyco.com.au</div>
      <div><svg width="16" height="12" viewBox="0 0 16 12"><rect width="16" height="12" rx="1" fill="#fff"/><path d="M1 1l7 5 7-5" fill="none" stroke="#1565c0" stroke-width="1.4"/></svg>info@klvsupplyco.com.au</div>
    </div>
    <div class="divider"></div>
    <div class="website">
      <svg width="18" height="18" viewBox="0 0 18 18"><g fill="none" stroke="#fff" stroke-width="1.4"><circle cx="9" cy="9" r="7.5"/><ellipse cx="9" cy="9" rx="3.3" ry="7.5"/><path d="M1.5 9h15M3 5h12M3 13h12"/></g></svg>
      www.klvmtq.com
    </div>
  </footer>

</div>
</body>
</html>
```